Bramwell Capabilities Brochure

I'm looking for a 6 page brochure, flat size 25.5" x 11", folds to 8.5" x 11".
I want this to highlight the capabilities of my printing business.
I've uploaded a brochure concept designed by my in-house designer that I was not crazy about. But thought it may be helpful in understanding the type of work we provide. I can also provide additional images. I do not want to use the panel for COVID related products.

```html
<!DOCTYPE html>
<html lang="en">
<head>
<meta charset="utf-8">
<title>Bramwell Capabilities Brochure</title>
<link href="https://fonts.googleapis.com/css2?family=Montserrat:ital,wght@0,400;0,500;1,600;1,700;1,800&display=swap" rel="stylesheet">
<style>
  :root{
    --red:#e3141b;
    --ink:#1b1b1b;
    --paper:#f1f1f1;
    --paper-shade:#e4e4e4;
    --stage:#d8d8d8;
    --edge:#151515;
    --white:#ffffff;
  }
  *{box-sizing:border-box;margin:0;padding:0}
  html,body{width:1200px;height:768px;overflow:hidden}
  body{background:var(--stage);font-family:"Montserrat",Arial,sans-serif;color:var(--ink);position:relative}
  .spread{position:absolute;left:0;top:125px;width:1200px;height:518px;display:flex;box-shadow:0 10px 30px rgba(0,0,0,.18)}
  .panel{position:relative;width:400px;height:518px;background:linear-gradient(160deg,var(--paper) 0%,var(--paper-shade) 100%);overflow:hidden}
  .panel + .panel{border-left:1px solid #d0d0d0}
  .panel::after{content:"";position:absolute;left:0;right:0;bottom:0;height:7px;background:var(--edge)}

  .tab{position:absolute;height:20px;background:var(--red);color:var(--white);font-style:italic;font-weight:800;font-size:10px;letter-spacing:.06em;text-transform:uppercase;line-height:20px;padding-left:14px;clip-path:polygon(0 0,100% 0,calc(100% - 12px) 100%,0 100%)}
  .rule{position:absolute;height:1.5px;background:var(--red)}
  .site{position:absolute;right:14px;font-size:7px;font-weight:600;font-style:italic;color:var(--ink)}

  .services{position:absolute;list-style:none;font-style:italic;font-weight:700;font-size:9.5px;line-height:13px}
  .services li{position:relative;padding-left:13px}
  .services li::before{content:"";position:absolute;left:0;top:3px;width:7px;height:7px;border:1.3px solid var(--red);border-radius:50%}
  .services.compact{font-size:8.5px;line-height:11.5px}
  .services.compact li::before{top:2px;width:6px;height:6px}

  .photo{position:absolute;border:2px solid var(--white);box-shadow:0 1px 3px rgba(0,0,0,.25)}

  .about{position:absolute;left:20px;top:378px;width:228px;font-size:7px;line-height:10px;font-weight:500;font-style:italic}

  .contact-bar{position:absolute;left:40px;right:40px;bottom:18px;height:17px;background:var(--red);border-radius:9px;color:var(--white);font-size:8px;font-weight:600;display:flex;align-items:center;justify-content:center;gap:10px}
  .contact-bar svg{width:8px;height:8px;vertical-align:-1px;margin-right:3px}
  .contact-bar .sep{opacity:.8}
</style>
</head>
<body>
<main class="spread">

  <!-- Panel: Corporate Collateral -->
  <section class="panel panel-collateral">
    <h2 class="tab" style="left:30px;top:18px;width:215px">Corporate Collateral</h2>
    <div class="rule" style="left:240px;top:37px;right:10px"></div>
    <p class="site" style="top:42px">www.bramwellprintgraphics.com</p>
    <ul class="services" style="left:34px;top:44px">
      <li>Brochures, Postcards</li>
      <li>Business Stationary</li>
      <li>Mailing Services</li>
      <li>NCR and Business Forms</li>
      <li>Business Labels</li>
      <li>Variable Data Printing</li>
      <li>Promotional Items</li>
    </ul>
    <div class="photo" role="img" aria-label="Stack of multi-part business forms" style="left:20px;top:140px;width:155px;height:62px;background:linear-gradient(135deg,#dfe5ee,#aab6c8)"></div>
    <div class="photo" role="img" aria-label="Fanned colourful presentation folders" style="left:20px;top:206px;width:155px;height:80px;background:linear-gradient(135deg,#c0392b,#e8b23a 45%,#3c6e3c 75%,#2c2c2c)"></div>
    <div class="photo" role="img" aria-label="Branded stationery set with pens" style="left:198px;top:118px;width:92px;height:68px;background:linear-gradient(135deg,#f4f4f4,#c8c8c8)"></div>
    <div class="photo" role="img" aria-label="Letterhead and envelopes on a desk" style="left:294px;top:140px;width:92px;height:68px;background:linear-gradient(135deg,#8a6b4a,#e9e3da)"></div>
    <div class="photo" role="img" aria-label="Stack of printed postcards with a meadow scene" style="left:182px;top:190px;width:205px;height:148px;background:linear-gradient(135deg,#e8eef2,#8fb35a 55%,#2f6b2f)"></div>
    <div class="photo" role="img" aria-label="Promotional items: pens, mug, calendar, tote bag and cap" style="left:20px;top:290px;width:158px;height:82px;background:linear-gradient(135deg,#f5f5f5,#d6c49a 50%,#2a3a55)"></div>
    <div class="photo" role="img" aria-label="Black restaurant menu cards" style="left:256px;top:344px;width:130px;height:96px;background:linear-gradient(135deg,#f2f2f2 30%,#1e1e1e 31%,#303030)"></div>
    <p class="about">At Bramwell Printing and Graphics, we have a unique offering of products and services. We also have the experience, resources, and technology to meet the stringent demands facing today's business community. To large businesses, we provide a virtual marketing department that keeps costs down, quality high, and marketing consistent. For our smaller clients, we deliver access to unparalleled expertise, equipment, and marketing options.</p>
    <footer class="contact-bar">
      <span><svg viewBox="0 0 10 10"><circle cx="5" cy="5" r="4.3" fill="none" stroke="#fff" stroke-width="1"/><path d="M3.3 3c.2 1.7 1.3 3.2 3.4 3.9l.6-.8-.9-.6-.5.4c-.7-.4-1.2-1-1.4-1.6l.4-.5-.6-.9z" fill="#fff"/></svg>(555) 310-4826</span>
      <span class="sep">|</span>
      <span><svg viewBox="0 0 10 10"><rect x="1" y="2.5" width="8" height="5.5" fill="none" stroke="#fff" stroke-width="1"/><path d="M1 2.5l4 3 4-3" fill="none" stroke="#fff" stroke-width="1"/></svg>info@bramwellprintgraphics.com</span>
    </footer>
  </section>

  <!-- Panel: Vehicle Graphics & Site Signage -->
  <section class="panel panel-vehicle">
    <h2 class="tab" style="left:22px;top:18px;width:225px">Vehicle Graphics &amp; Wraps</h2>
    <div class="rule" style="left:242px;top:37px;right:10px"></div>
    <p class="site" style="top:42px">www.bramwellprintgraphics.com</p>
    <ul class="services" style="left:26px;top:44px">
      <li>Decals</li>
      <li>Complete Wraps</li>
      <li>Compact Cars to Tankers</li>
      <li>Design</li>
    </ul>
    <div class="photo" role="img" aria-label="Wrapped rally pickup truck" style="left:20px;top:106px;width:128px;height:66px;background:linear-gradient(135deg,#2b2f35,#c8d23a 50%,#6e7680)"></div>
    <div class="photo" role="img" aria-label="Red compact car with full wrap" style="left:20px;top:176px;width:128px;height:68px;background:linear-gradient(135deg,#8d8d8d,#d8222a 50%,#5a5a5a)"></div>
    <div class="photo" role="img" aria-label="Fuel tanker truck with orange wrap" style="left:154px;top:100px;width:228px;height:88px;background:linear-gradient(180deg,#a9c4e0,#dfe8f1 40%,#c25a2a 60%,#4a4a4a)"></div>
    <div class="photo" role="img" aria-label="Yellow service van with lettering" style="left:154px;top:192px;width:110px;height:56px;background:linear-gradient(135deg,#7a9cc0,#e8c32a 55%,#3a3a3a)"></div>
    <div class="photo" role="img" aria-label="Blue crew van with graphics" style="left:268px;top:192px;width:114px;height:56px;background:linear-gradient(135deg,#9dbbd6,#1f5fae 55%,#e6ecf2)"></div>

    <h2 class="tab" style="left:12px;top:256px;width:175px">Site Signage</h2>
    <div class="rule" style="left:182px;top:275px;right:10px"></div>
    <ul class="services" style="left:18px;top:282px">
      <li>Permanent</li>
      <li>Temporary</li>
      <li>Flags</li>
      <li>Installation</li>
    </ul>
    <div class="photo" role="img" aria-label="Storefront window signage and banners" style="left:20px;top:338px;width:112px;height:130px;background:linear-gradient(135deg,#2a2a2a,#b8262a 45%,#d9a441 80%)"></div>
    <div class="photo" role="img" aria-label="Housing development sign on a lawn" style="left:136px;top:324px;width:118px;height:68px;background:linear-gradient(180deg,#9fbfd8,#f0f0f0 45%,#5c8a3c)"></div>
    <div class="photo" role="img" aria-label="Green and yellow open sign" style="left:258px;top:334px;width:124px;height:60px;background:linear-gradient(135deg,#4a4a4a,#2f7a3a 45%,#e8c23a 70%,#6a6a6a)"></div>
    <div class="photo" role="img" aria-label="Building facade signage" style="left:136px;top:396px;width:118px;height:72px;background:linear-gradient(135deg,#1f2a44,#3f5f9a 50%,#c9b48a)"></div>
    <div class="photo" role="img" aria-label="Stone monument sign with landscaping" style="left:258px;top:398px;width:124px;height:70px;background:linear-gradient(180deg,#a9b7a0,#8a7a6a 50%,#9a3a2a)"></div>
    <footer class="contact-bar">
      <span><svg viewBox="0 0 10 10"><circle cx="5" cy="5" r="4.3" fill="none" stroke="#fff" stroke-width="1"/><path d="M3.3 3c.2 1.7 1.3 3.2 3.4 3.9l.6-.8-.9-.6-.5.4c-.7-.4-1.2-1-1.4-1.6l.4-.5-.6-.9z" fill="#fff"/></svg>(555) 310-4826</span>
      <span class="sep">|</span>
      <span><svg viewBox="0 0 10 10"><rect x="1" y="2.5" width="8" height="5.5" fill="none" stroke="#fff" stroke-width="1"/><path d="M1 2.5l4 3 4-3" fill="none" stroke="#fff" stroke-width="1"/></svg>info@bramwellprintgraphics.com</span>
    </footer>
  </section>

  <!-- Panel: Interior/Exterior & Corporate Needs -->
  <section class="panel panel-interior">
    <h2 class="tab" style="left:14px;top:18px;width:240px">Interior/Exterior Graphics</h2>
    <div class="rule" style="left:250px;top:37px;right:10px"></div>
    <p class="site" style="top:25px">www.bramwellprintgraphics.com</p>
    <ul class="services compact" style="left:18px;top:44px">
      <li>Floor Decals</li>
      <li>Wall Wraps</li>
      <li>Display Graphics</li>
      <li>Window Clings and Perf</li>
      <li>Metal Signage</li>
      <li>POP Kits / Kit Packing</li>
      <li>Building Wraps or anything</li>
      <li>else you can think of...</li>
    </ul>
    <div class="photo" role="img" aria-label="Restaurant interior with wall graphics" style="left:176px;top:46px;width:208px;height:52px;background:linear-gradient(135deg,#3a2410,#d98a2a 50%,#2a1a0a)"></div>
    <div class="photo" role="img" aria-label="Sports-themed wall mural" style="left:176px;top:102px;width:100px;height:50px;background:linear-gradient(135deg,#1a1a1a,#c9952a 60%,#3a3a3a)"></div>
    <div class="photo" role="img" aria-label="Lounge with large wall print" style="left:280px;top:102px;width:104px;height:50px;background:linear-gradient(135deg,#4a2a10,#b86a2a 50%,#1a1a1a)"></div>
    <div class="photo" role="img" aria-label="Storefront with window graphics" style="left:16px;top:150px;width:156px;height:62px;background:linear-gradient(180deg,#c9c9c9,#b8262a 45%,#3a3a3a)"></div>
    <div class="photo" role="img" aria-label="Retail interior with red displays" style="left:176px;top:156px;width:104px;height:58px;background:linear-gradient(135deg,#d8d8d8,#c0262a 50%,#8a8a8a)"></div>
    <div class="photo" role="img" aria-label="Building exterior with banner sign" style="left:284px;top:156px;width:100px;height:58px;background:linear-gradient(180deg,#6a9ad0,#2a5a9a 50%,#6a8a4a)"></div>

    <h2 class="tab" style="left:8px;top:224px;width:175px">Corporate Needs</h2>
    <div class="rule" style="left:178px;top:243px;right:10px"></div>
    <ul class="services compact" style="left:14px;top:250px">
      <li>Tradeshow / Event</li>
      <li>Retractables</li>
      <li>Wallpaper</li>
      <li>Window Graphics</li>
      <li>Wall Art</li>
    </ul>
    <div class="photo" role="img" aria-label="Office lobby with printed wall display" style="left:176px;top:250px;width:104px;height:80px;background:linear-gradient(135deg,#2a2a2a,#9aa8b8 50%,#d8dde2)"></div>
    <div class="photo" role="img" aria-label="Tradeshow booth backdrop" style="left:284px;top:250px;width:100px;height:62px;background:linear-gradient(135deg,#0f1e3a,#2a5ab0 55%,#1a1a1a)"></div>
    <div class="photo" role="img" aria-label="Hallway lined with framed wall art" style="left:16px;top:330px;width:150px;height:110px;background:linear-gradient(135deg,#3a2a1a,#a88a6a 50%,#d8d0c4)"></div>
    <div class="photo" role="img" aria-label="Lit gallery wall with mounted prints" style="left:170px;top:334px;width:108px;height:100px;background:linear-gradient(180deg,#2a2a2a,#e8d8a8 40%,#5a5a5a)"></div>
    <div class="photo" role="img" aria-label="Retractable banner stand and window graphic" style="left:282px;top:316px;width:102px;height:120px;background:linear-gradient(135deg,#e0e0e0,#8a8a8a 50%,#2a2a2a)"></div>
    <footer class="contact-bar">
      <span><svg viewBox="0 0 10 10"><circle cx="5" cy="5" r="4.3" fill="none" stroke="#fff" stroke-width="1"/><path d="M3.3 3c.2 1.7 1.3 3.2 3.4 3.9l.6-.8-.9-.6-.5.4c-.7-.4-1.2-1-1.4-1.6l.4-.5-.6-.9z" fill="#fff"/></svg>(555) 310-4826</span>
      <span class="sep">|</span>
      <span><svg viewBox="0 0 10 10"><rect x="1" y="2.5" width="8" height="5.5" fill="none" stroke="#fff" stroke-width="1"/><path d="M1 2.5l4 3 4-3" fill="none" stroke="#fff" stroke-width="1"/></svg>info@bramwellprintgraphics.com</span>
    </footer>
  </section>

</main>
</body>
</html>
```